10' x 4' outdoor vinyl banner

My company prepare and sell delicious Maryland Style Gourmet Crab Cake sandwiches at public events like fairs, festivals and concerts.
We use a 10' x 10' tent to prepare and sell this sandwiches at those events. I need a 10x4 (10 feet long by 4 feet high) banner display for the top of the tent. The same design should be scalable to another 10x3 banner for the bottom of the tent.
I need a general design of a banner with a wording that should be very attention catching
The wording is: "Maryland Crab Cake Sandwiches"
I would like also to incorporate into the design a blue crab (this is the name of specific type of crab that I'm looking for, is not just a crab painted in blue)
The theme of the design should be the sea, the shoreline, maybe some fishing boat, waves, etc, in that spirit.
I would like to use a nice blue color in the background, as we are talking about the sea and marine themes.
There are some other wordings that I would like to incorporate into the banner:
A Traditional Chesapeake Bay recipe with 100% All Natural, Blue Crab Meat . . . Rich and Flavorful . . .
This type should be in smaller size, but still visible, maybe in italics or an elegant font type.
I want something simple, inviting, like my delicious sandwiches.

```html
<!DOCTYPE html>
<html lang="en">
<head>
<meta charset="utf-8">
<title>Maryland Crab Cake Sandwiches Banner</title>
<link rel="stylesheet" href="https://fonts.googleapis.com/css2?family=Nunito:wght@700;800&family=Fira+Sans+Extra+Condensed:wght@700&display=swap">
<style>
  :root {
    --navy: #2b2a7f;
    --sky-blue: #5cbcf0;
    --white: #ffffff;
    --bun: #e8d3b4;
    --crab-shell: #9a8f7c;
    --frame-dark: #3a2616;
    --frame-light: #6b4a2c;
    --harbor-sky: #c9c8c2;
    --harbor-water: #6f7478;
  }
  html, body {
    margin: 0;
    padding: 0;
    overflow: hidden;
    background: var(--white);
  }
  .banner {
    position: relative;
    width: 1200px;
    height: 480px;
    overflow: hidden;
    background: var(--white);
    font-family: "Nunito", sans-serif;
  }
  .food-photo {
    position: absolute;
    left: 0;
    top: 0;
    width: 500px;
    height: 480px;
    background:
      radial-gradient(ellipse 170px 190px at 190px 290px, #d9a774 0%, #e9cfae 45%, rgba(255,255,255,0) 100%),
      radial-gradient(ellipse 140px 110px at 150px 60px, #d8b48c 0%, rgba(255,255,255,0) 100%),
      linear-gradient(90deg, var(--bun) 0%, #f1e6d6 55%, var(--white) 100%);
  }
  .band {
    position: absolute;
    left: 398px;
    width: 802px;
    background: var(--navy);
    color: var(--white);
    box-sizing: border-box;
  }
  .band--top {
    top: 9px;
    height: 77px;
  }
  .band--bottom {
    top: 261px;
    height: 78px;
  }
  .state-name {
    position: absolute;
    left: 40px;
    top: 8px;
    margin: 0;
    font-size: 46px;
    font-weight: 800;
    letter-spacing: 1px;
    line-height: 1.2;
  }
  .product-type {
    position: absolute;
    left: 40px;
    top: 4px;
    margin: 0;
    font-size: 56px;
    font-weight: 700;
    letter-spacing: 4px;
    line-height: 1.2;
  }
  .headline {
    position: absolute;
    left: 414px;
    top: 82px;
    margin: 0;
    font-size: 142px;
    font-weight: 800;
    color: var(--navy);
    line-height: 1.2;
    letter-spacing: -2px;
    text-shadow: -9px 3px 0 var(--sky-blue);
  }
  .crab-photo {
    position: absolute;
    left: 862px;
    top: 0;
    width: 330px;
    height: 165px;
    border-radius: 50%;
    background: radial-gradient(ellipse at 50% 50%, var(--crab-shell) 0%, #b7b0a2 45%, rgba(255,255,255,0) 72%);
  }
  .tagline {
    position: absolute;
    left: 426px;
    top: 350px;
    margin: 0;
    font-family: "Fira Sans Extra Condensed", sans-serif;
    font-weight: 700;
    font-size: 28px;
    line-height: 34px;
    color: var(--navy);
  }
  .harbor-frame {
    position: absolute;
    left: 952px;
    top: 284px;
    width: 260px;
    height: 210px;
    transform: rotate(-3deg);
    box-sizing: border-box;
    border: 14px solid var(--frame-dark);
    outline: 3px solid var(--frame-light);
    outline-offset: -10px;
    box-shadow: 2px 3px 6px rgba(0,0,0,0.35);
  }
  .harbor-photo {
    width: 100%;
    height: 100%;
    background: linear-gradient(180deg, var(--harbor-sky) 0%, #dcdad3 45%, #8e8f8c 62%, var(--harbor-water) 100%);
  }
</style>
</head>
<body>
  <main class="banner">
    <div class="food-photo" role="img" aria-label="Crab cake slider sandwiches with lettuce and mustard sauce on soft buns"></div>

    <div class="band band--top">
      <h2 class="state-name">Maryland</h2>
    </div>

    <div class="crab-photo" role="img" aria-label="Chesapeake blue crab with claws spread"></div>

    <h1 class="headline">Crab Cake</h1>

    <div class="band band--bottom">
      <h2 class="product-type">Sandwiches</h2>
    </div>

    <p class="tagline">A Traditional Chesapeake Bay recipe with<br>100% All Natural, Blue Crab Meat . . .<br>Rich and Flavorful</p>

    <div class="harbor-frame">
      <div class="harbor-photo" role="img" aria-label="Fishing boat moored at a harbor pier at dusk"></div>
    </div>
  </main>
</body>
</html>
```